Lead Generation Postcard Design for Digital Agency Targeting Eye Care Practices

We are a digital marketing agency looking to build our business by offering digital marketing services to a niche market - eye doctors, optometrists. We want to offer them our services and offer a free phone consulting session. They can either call us or visit our web site contact us form (http://www.brightkestrelmedia.com/contact-us/)We would like to have a design that matches our web site colors, theme, look and feel. But we also want to communicate the eye care industry and somehow the idea of 'digital marketing'.The goal is to get the company to call or contact us for further information.We have saved an example postcard in our account that you can take a look at.

Target Market(s)

eye doctors, optometry practices

Industry/Entity Type

Digital

Font styles to use
Other font styles liked:
• see web site for examples

Requirements
Must have
• Big 'gotcha' image.
• matches the look and feel of our web site (www.brightkestrelmedia.com).
• will send logo when our designer provides... asap.
Should not have
• cheesy looking stock images.

```html
<!DOCTYPE html>
<html lang="en">
<head>
<meta charset="utf-8">
<title>Bright Kestrel Media – Eye Care Postcard</title>
<link href="https://fonts.googleapis.com/css2?family=Roboto+Slab:wght@800;900&family=Ubuntu:wght@400;500;700&display=swap" rel="stylesheet">
<style>
  :root {
    --navy: #1d5170;
    --navy-deep: #163f58;
    --red: #e8342f;
    --ink: #234a68;
    --white: #ffffff;
    --mist: #eef0f2;
    --rule: #9fb3c4;
    --sky-1: #5fb2d6;
    --sky-2: #1f6e98;
    --sky-3: #0b2a40;
  }
  * { box-sizing: border-box; margin: 0; padding: 0; }
  html, body { width: 1200px; height: 435px; overflow: hidden; background: #ffffff; }
  body { position: relative; font-family: "Ubuntu", sans-serif; }

  .card { position: absolute; top: 8px; height: 419px; overflow: hidden; }

  /* Front */
  .front { left: 6px; width: 591px; }
  .hero-photo {
    position: absolute; inset: 0;
    background:
      radial-gradient(ellipse 55% 60% at 80% 45%, rgba(5,20,32,.85), transparent 70%),
      radial-gradient(ellipse 60% 55% at 25% 35%, rgba(150,215,240,.6), transparent 70%),
      radial-gradient(ellipse 50% 40% at 30% 85%, rgba(120,190,220,.45), transparent 70%),
      linear-gradient(100deg, var(--sky-1) 0%, var(--sky-2) 50%, var(--sky-3) 100%);
  }
  .headline {
    position: absolute; left: 0; right: 0; top: 10px; text-align: center;
    font-family: "Roboto Slab", serif; font-weight: 900; color: var(--white);
  }
  .headline .line-1 { display: block; font-size: 28px; line-height: 32px; letter-spacing: 2.4px; }
  .headline .line-2 { display: block; font-size: 20px; line-height: 28px; letter-spacing: 2px; margin-top: 4px; }
  .headline .accent { color: var(--red); }
  .brand-mark {
    position: absolute; left: 22px; bottom: 22px; display: flex; align-items: center; gap: 8px;
  }
  .brand-mark .dot { width: 26px; height: 26px; border-radius: 50%; background: var(--red); }
  .brand-mark .name { font-weight: 700; font-size: 26px; color: var(--white); line-height: 1; }
  .front-contact { position: absolute; right: 22px; bottom: 14px; text-align: right; color: var(--white); }
  .front-contact .phone { display: flex; align-items: center; justify-content: flex-end; gap: 14px; font-size: 31px; line-height: 34px; }
  .front-contact .phone svg { width: 28px; height: 28px; }
  .front-contact .url { font-size: 12px; margin-top: 6px; }

  /* Back */
  .back { left: 605px; width: 590px; background: var(--white); border: 1px solid #e3e6e9; }
  .message { position: absolute; left: 0; top: 0; width: 335px; height: 100%; }
  .message-head {
    height: 75px; background: var(--navy); text-align: center;
    font-family: "Roboto Slab", serif; font-weight: 800; padding-top: 14px; letter-spacing: .6px;
  }
  .message-head .title { color: var(--white); font-size: 14px; line-height: 20px; }
  .message-head .accent { color: var(--red); font-size: 14px; line-height: 20px; }
  .intro {
    margin: 11px 18px 0 20px; font-size: 10px; line-height: 15px; color: var(--ink);
    text-align: justify;
  }
  .services {
    list-style: none; display: grid; grid-template-columns: 155px 150px;
    row-gap: 9px; margin: 16px 0 0 28px;
  }
  .services li { display: flex; align-items: center; gap: 10px; font-size: 7.5px; color: var(--ink); text-transform: uppercase; height: 17px; }
  .services svg { width: 18px; height: 17px; flex: none; }

  .office {
    position: absolute; left: 0; top: 273px; width: 335px; height: 103px;
    background: var(--navy); color: var(--white); padding: 15px 0 0 18px;
  }
  .office .company { font-size: 17px; line-height: 20px; }
  .office address { font-style: normal; font-size: 10.5px; line-height: 13px; }
  .office .map {
    position: absolute; left: 185px; top: 8px; width: 140px; height: 86px;
    background: linear-gradient(135deg, #e8e5da, #dadfd0);
  }
  .contact-strip {
    position: absolute; left: 0; top: 377px; width: 335px; height: 35px;
    background: var(--mist); color: var(--ink); display: flex; align-items: center; padding-left: 18px;
  }
  .contact-strip .lines { font-size: 10.5px; line-height: 13px; width: 124px; }
  .contact-strip .brace { font-size: 34px; font-weight: 300; line-height: 1; width: 26px; color: var(--navy); }
  .contact-strip .url { font-size: 8.5px; }
  .base-band { position: absolute; left: 0; bottom: 0; width: 335px; height: 7px; background: var(--navy-deep); }

  .mailing { position: absolute; left: 335px; top: 0; width: 255px; height: 100%; }
  .stamp { position: absolute; left: 158px; top: 12px; width: 74px; height: 88px; border: 1px solid var(--rule); }
  .address-line { position: absolute; left: 20px; width: 212px; height: 1px; background: var(--rule); }
</style>
</head>
<body>

<section class="card front">
  <div class="hero-photo" role="img" aria-label="Big dramatic full-bleed image: rain-soaked blue scene with a dark figure clinging on the right"></div>
  <h1 class="headline">
    <span class="line-1">GROW YOUR EYE CARE PRACTICE</span>
    <span class="line-2">WITH <span class="accent">DITITAL MARKETING</span></span>
  </h1>
  <div class="brand-mark"><span class="dot"></span><span class="name">Bright Kestrel</span></div>
  <div class="front-contact">
    <div class="phone">
      <svg viewBox="0 0 28 28"><rect x="0" y="0" width="28" height="28" rx="5" fill="#fff"/><path d="M9 6c-2 1-3 3-2 6 1 4 4 8 8 10 2 1 4 0 5-2l-3-3-2 1c-2-1-4-4-4-6l1-2-3-4z" fill="#1d5170"/></svg>
      <span>816-555-0142</span>
    </div>
    <div class="url">www.brightkestrelmedia.com</div>
  </div>
</section>

<section class="card back">
  <div class="message">
    <header class="message-head">
      <div class="title">WE HELP YOUR EYE CARE PRACTICE</div>
      <div class="accent">SEE MORE PATIENTS</div>
    </header>
    <p class="intro">We’re a seasoned digital marketing agency for eye care practices. We’ve been helping optometrists and eye doctors fill their schedules for as long as online search has been around. With our unique, ‘outside the box’ mindset and our proven suite of digital marketing services, your practice may be seeing new patients within days. Call now for a free phone consultation.</p>
    <ul class="services">
      <li><svg viewBox="0 0 18 17" fill="none" stroke="#e8342f" stroke-width="1.2"><rect x="1.5" y="5" width="15" height="10" rx="1"/><path d="M6 5V3h6v2M1.5 9h15"/></svg>Client case studies</li>
      <li><svg viewBox="0 0 18 17" fill="none" stroke="#e8342f" stroke-width="1.2"><path d="M1 2h3l2 9h9l2-6H5"/><circle cx="7" cy="14" r="1.3"/><circle cx="14" cy="14" r="1.3"/></svg>Website marketing</li>
      <li><svg viewBox="0 0 18 17" fill="none" stroke="#e8342f" stroke-width="1.2"><rect x="1.5" y="2" width="12" height="9" rx="1.5"/><path d="M4 11v3l3-3M6 13h8l2 2v-8h-2"/></svg>Social media</li>
      <li><svg viewBox="0 0 18 17" fill="none" stroke="#e8342f" stroke-width="1.4"><circle cx="7" cy="7" r="5"/><path d="M11 11l5 5"/></svg>Search engine optimization</li>
      <li><svg viewBox="0 0 18 17" fill="none" stroke="#e8342f" stroke-width="1.2"><circle cx="8" cy="8" r="6.5"/><circle cx="8" cy="8" r="3"/><path d="M8 8l7 3-3 1-1 3z" fill="#e8342f"/></svg>Paid search marketing</li>
    </ul>
    <div class="office">
      <div class="company">Bright Kestrel</div>
      <address>Bright Kestrel Media, LLC<br>4120 Larkspur Avenue,<br>18 Meadow Plaza, Suite 210<br>Fairview, KS. 66099</address>
      <div class="map" role="img" aria-label="Street map showing the office location"></div>
    </div>
    <div class="contact-strip">
      <div class="lines">CALL : 816-555-0142<br>FAX : 816-555-0187</div>
      <div class="brace">}</div>
      <div class="url">www.brightkestrelmedia.com</div>
    </div>
    <div class="base-band"></div>
  </div>
  <div class="mailing">
    <div class="stamp"></div>
    <div class="address-line" style="top:170px"></div>
    <div class="address-line" style="top:205px"></div>
    <div class="address-line" style="top:241px"></div>
    <div class="address-line" style="top:276px"></div>
  </div>
</section>

</body>
</html>
```